Paws and Meadows is a dog walking service that offers home boarding and pet taxi

I am looking for a eye catching A5 leaflet/flyer design for my dog walking business Paws and Meadows.

The flyer must have my company logo on it (jpeg), a picture of my van (jpeg) and a picture of dogs playing (jpegs 1-5).

The fonts must be easy to read. I am not set on any colour scheme but do like the idea of having a natural background. IE. Green grass and blue sky or some forest setting with green trees. If you don't like this idea or its hard to work with don't worry I am open minded so be creative and do what you thinks best.

I'll provide quick feedback to designs that i like and so we can work together.

The flyers must contain the following:

60 minute group and individual walks
GPS Tracked Walks
Home Boarding
Pet Taxi
Puppy/Pet visits

Offer: 50% off first weeks dogs walks with this flyer.

As well as containing my contact info:

07915382046
www.paws-and-meadows.co.uk
paws-and-meadows@mailbrook.co.uk

Chatterbook, Chirpline and Snapgallery logos must be present as well.

Thanks and Good luck!

Target Market(s)

ANYONE WHO NEEDS THEIR DOG WALKED OR LOOKED AFTER WHEN THEY ARE ON HOLIDAY

Industry/Entity Type

Business

Contact Information for Business Card

THE BUSINESS CARD MUST DISPLAY THE LOGO THAT HAS BEEN UPLOADED IN A FILE. IT MUST LOOK SHARP AND PROFESSIONAL. CONTAIN ALL CONTACT INFO AND HAVE SERVICES OFFERED. SEE PROJECT DESCRIPTION FOR FLYER.

Font styles to use
Serif
Sans Serif

Requirements
Must have
• SEE PROJECT DESCRIPTION
Nice to have
• IT WOULD BE NICE TO HAVE PHOTOS OF MY VAN AND DOGS PLAYING. I HAVE UPLOADED SOME PICS OF VAN TO BE USED AND THERE ARE PICS OF DOGS PLAYING THAT COULD BE USED.

```html
<!DOCTYPE html>
<html lang="en">
<head>
<meta charset="utf-8">
<title>Paws and Meadows – Dog Walking Flyer</title>
<link rel="stylesheet" href="https://fonts.googleapis.com/css2?family=Roboto:wght@400;700;900&display=swap">
<style>
  :root {
    --page-bg: #e8e4df;
    --paper: #ffffff;
    --meadow: #3b8526;
    --meadow-text: #2f7a1c;
    --sky: #3aa8f0;
    --logo-sun: #f2a93b;
    --logo-ink: #3d4a4f;
    --white: #ffffff;
  }
  * { margin: 0; padding: 0; box-sizing: border-box; }
  html, body {
    width: 1200px; height: 960px; overflow: hidden;
    background: var(--page-bg);
    font-family: "Roboto", Arial, sans-serif;
  }
  .flyer {
    position: absolute; left: 275px; top: 20px;
    width: 650px; height: 920px;
    background: var(--paper);
    overflow: hidden;
    box-shadow: 0 6px 24px rgba(0,0,0,0.12);
  }
  .photo { position: absolute; }
  .photo--van {
    left: 0; top: 0; width: 650px; height: 420px;
    clip-path: polygon(330px 0, 650px 0, 650px 290px, 480px 290px, 480px 420px, 140px 420px);
    background: linear-gradient(180deg, #5fa8e8 0%, #9ccdf2 30%, #8fb0a8 52%, #5f9f3a 70%, #3f8a2a 100%);
  }
  .photo--stick { left: 490px; top: 300px; width: 160px; height: 120px;
    background: linear-gradient(160deg, #a6b58a 0%, #8a7a5c 50%, #5d6b3c 100%); }
  .photo--field { left: 490px; top: 430px; width: 160px; height: 250px;
    background: linear-gradient(180deg, #9dc98a 0%, #62a83a 40%, #3f8f25 100%); }
  .photo--pair { left: 140px; top: 550px; width: 105px; height: 130px;
    background: linear-gradient(180deg, #6d9b4c 0%, #4b8a2e 60%, #3d7a24 100%); }
  .photo--greyhound { left: 253px; top: 550px; width: 107px; height: 130px;
    background: linear-gradient(180deg, #4f7e34 0%, #b98a4a 55%, #5a8a33 100%); }
  .photo--tree { left: 368px; top: 550px; width: 112px; height: 130px;
    background: linear-gradient(180deg, #cfe0ea 0%, #c9c0a6 45%, #5f9a35 100%); }

  .logo {
    position: absolute; left: 34px; top: 118px;
    display: flex; align-items: center; gap: 12px;
  }
  .logo__mark { width: 54px; height: 54px; border-radius: 50%; background: var(--logo-sun); }
  .logo__name { font-weight: 700; font-size: 24px; color: var(--logo-ink); }

  .offer {
    position: absolute; left: 140px; top: 430px; width: 340px; height: 110px;
    background: var(--sky);
    color: var(--white);
    font-weight: 900; font-size: 23px; line-height: 1.25;
    display: flex; align-items: center; padding: 0 24px;
  }

  .services {
    position: absolute; left: 40px; top: 720px;
    list-style: none;
    color: var(--meadow-text);
    font-weight: 700; font-size: 17px; line-height: 1.3;
  }

  .social {
    position: absolute; left: 40px; top: 868px;
    display: flex; gap: 18px; list-style: none;
  }
  .social__item { display: flex; align-items: center; gap: 6px;
    font-weight: 700; font-size: 12px; color: var(--sky); }
  .social__dot { width: 22px; height: 22px; border-radius: 50%; background: var(--sky); }

  .contact {
    position: absolute; left: 0; top: 0; width: 650px; height: 920px;
    clip-path: polygon(360px 692px, 650px 692px, 650px 920px, 385px 920px);
    background: var(--meadow);
  }
  .contact__body {
    position: absolute; right: 22px; top: 740px;
    text-align: right; color: var(--white);
    font-weight: 700; font-size: 14px; line-height: 1.45;
  }
  .contact__title { font-size: 17px; margin-bottom: 10px; }
</style>
</head>
<body>
  <main class="flyer">
    <div class="photo photo--van" role="img" aria-label="Photo of the branded dog walking van on green grass under a blue sky"></div>
    <div class="photo photo--stick" role="img" aria-label="Photo of two dogs carrying a stick together"></div>
    <div class="photo photo--field" role="img" aria-label="Photo of a group of dogs running across a park field"></div>
    <div class="photo photo--pair" role="img" aria-label="Photo of two greyhounds resting in long grass"></div>
    <div class="photo photo--greyhound" role="img" aria-label="Photo of a tan greyhound standing in a park"></div>
    <div class="photo photo--tree" role="img" aria-label="Photo of a dog lying in the grass beneath a tree"></div>

    <div class="logo">
      <span class="logo__mark" aria-hidden="true"></span>
      <span class="logo__name">Paws and Meadows</span>
    </div>

    <div class="offer">50% off first weeks dogs walks with this flyer.</div>

    <ul class="services">
      <li>60 minute group &amp; individual walks</li>
      <li>GPS Tracked Walks</li>
      <li>Home Boarding</li>
      <li>Pet Taxi</li>
      <li>Puppy/Pet visits</li>
    </ul>

    <ul class="social">
      <li class="social__item"><span class="social__dot"></span>Chatterbook</li>
      <li class="social__item"><span class="social__dot"></span>Chirpline</li>
      <li class="social__item"><span class="social__dot"></span>Snapgallery</li>
    </ul>

    <section class="contact">
      <div class="contact__body">
        <p class="contact__title">Contact Info:</p>
        <p>07915382046</p>
        <p>www.paws-and-meadows.co.uk</p>
        <p>paws-and-meadows@mailbrook.co.uk</p>
      </div>
    </section>
  </main>
</body>
</html>
```